Larkspur Ridge Management - Business Cards

I need business cards. My current logo was designed by a designer at this site and I very much like and am happy with the results. I would like a business card that is trendy, unique, current yet professional. I deal with high net worth clients daily

Target Market(s)

Out of state investors looking to get into the rental market in Ohio

Industry/Entity Type

Property Management, Consulting

Contact Information for Business Card

Name, Title (Chief Financial Officer) office phone number (555) 817-3094 website address larkridgemgmt.example

Font styles to use
Sans Serif

Colors
0054AA
0677BA
7BADD7
CADEEF
E8F1F8
0094D4
00A9DD
6FCCEA
C7EBF8
E9F6FB
00AB8E
00BBA5
67D7C9
C6EFE9
E9F9F6

```html
<!DOCTYPE html>
<html lang="en">
<head>
<meta charset="utf-8">
<title>Larkspur Ridge Management – Business Cards</title>
<link rel="stylesheet" href="https://fonts.googleapis.com/css2?family=Arimo:wght@400;700&display=swap">
<style>
  :root {
    --backdrop: #dedfe1;
    --navy: #1c3557;
    --red: #d42331;
    --white: #ffffff;
  }
  html, body {
    margin: 0;
    padding: 0;
    width: 1200px;
    height: 1200px;
    overflow: hidden;
    background: var(--backdrop);
  }
  .sheet {
    position: relative;
    width: 1200px;
    height: 1200px;
    font-family: "Arimo", Arial, sans-serif;
  }
  .card {
    position: absolute;
    left: 242px;
    width: 716px;
    height: 409px;
    display: block;
  }
  .card--front { top: 132px; }
  .card--back  { top: 600px; }
  .fill-navy  { fill: var(--navy); }
  .fill-red   { fill: var(--red); }
  .fill-white { fill: var(--white); }
  .brand-disc {
    fill: var(--navy);
    stroke: var(--white);
    stroke-width: 8;
  }
  .holder-name {
    font-weight: 700;
    font-size: 76px;
    fill: var(--white);
  }
  .holder-title {
    font-weight: 400;
    font-size: 34px;
    fill: var(--white);
  }
  .contact-text {
    font-weight: 400;
    font-size: 30px;
    fill: var(--white);
  }
  .brand-front {
    font-weight: 700;
    font-size: 46px;
    fill: var(--navy);
  }
  .brand-back {
    font-weight: 700;
    font-size: 42px;
    fill: var(--white);
  }
  .icon-line {
    fill: none;
    stroke: var(--white);
    stroke-width: 2.4;
  }
</style>
</head>
<body>
<main class="sheet">

  <!-- Front of card -->
  <svg class="card card--front" viewBox="0 0 1153 659" role="img" aria-label="Front of business card for Larkspur Ridge Management">
    <rect class="fill-white" x="0" y="0" width="1153" height="659"/>
    <polygon class="fill-navy" points="269,0 1153,0 1153,480 679,480"/>
    <polygon class="fill-red" points="364,591 539,413 656,532 1153,532 1153,591 634,591 539,495 444,591"/>
    <polygon class="fill-navy" points="0,453 453,453 396,512 0,512"/>
    <polygon class="fill-red" points="0,532 383,532 327,591 0,591"/>

    <g class="brand-wordmark" text-anchor="middle">
      <text class="brand-front" x="201" y="250">Larkspur Ridge</text>
      <text class="brand-front" x="201" y="306">Management</text>
    </g>

    <text class="holder-name" x="606" y="255">YOUR NAME</text>
    <text class="holder-title" x="626" y="316">Chief Financial Officer</text>

    <g class="icon-globe" transform="translate(29 483)">
      <circle class="icon-line" r="16"/>
      <ellipse class="icon-line" rx="7" ry="16"/>
      <line class="icon-line" x1="-16" y1="0" x2="16" y2="0"/>
      <line class="icon-line" x1="0" y1="-16" x2="0" y2="16"/>
      <line class="icon-line" x1="-13" y1="-8" x2="13" y2="-8"/>
      <line class="icon-line" x1="-13" y1="8" x2="13" y2="8"/>
    </g>
    <text class="contact-text" x="68" y="493">larkridgemgmt.example</text>

    <g class="icon-phone" transform="translate(36 563)">
      <path class="fill-white" d="M-10,-12 l6,-2 l5,9 l-4,4 q3,7 10,10 l4,-4 l9,5 l-2,6 q-4,3 -10,1 q-14,-6 -20,-20 q-2,-6 2,-9 z"/>
    </g>
    <text class="contact-text" x="65" y="575">(555) 817-3094</text>
  </svg>

  <!-- Back of card -->
  <svg class="card card--back" viewBox="0 0 1166 666" role="img" aria-label="Back of business card for Larkspur Ridge Management">
    <rect class="fill-white" x="0" y="0" width="1166" height="666"/>
    <polygon class="fill-navy" points="0,36 422,36 573,187 94,666 0,666"/>
    <polygon class="fill-navy" points="961,0 1166,0 1166,630 634,630 482,478"/>
    <circle class="brand-disc" cx="527" cy="334" r="178"/>
    <g class="brand-wordmark" text-anchor="middle">
      <text class="brand-back" x="527" y="322">Larkspur Ridge</text>
      <text class="brand-back" x="527" y="376">Management</text>
    </g>
  </svg>

</main>
</body>
</html>
```